BRAMLEIGH real estate family office

Hello, Our business is a real estate intermediation activity on high-end goods (amounts exceeding € 10m) for corporate and private clients. You can see our logo on the site www.bramleigh-invented.fr We would like to keep that spirit with the hexagon that represents France (transactions between Monaco and Saint Tropez, Courchevel and Paris). And the "baseline" that is "real estate family office". The corporate logo should be and can be printed by embossing (relief). We must integrate the name, first name, phone, email and website. Finally, to imbibe the spirit of business, here is a detail of the activity. "Genuine consulting firm in real estate investments, BRAMLEIGH works with its customers as a specialized player in the high-end markets, we are recognized for our ultra-confidential approach and tailor-made, as well as the quality of our network. We broadcast any information on the market and we work exclusively through a strong relationship we have developed over the years. BRAMLEIGH is active on the French Riviera (from Monaco to Saint-Tropez), the Alps (Courchevel, Méribel, Megève) and Paris (essentially market premium). Always looking for opportunities for our clients, we work on two investment areas: residential luxury real estate (properties, vineyards, mansions, land, etc.) commercial real estate (empty office buildings or yield, hotel properties, land, etc.) "

Target Market(s)

High foreign end customers. corporate and private.

Industry/Entity Type

Real Estate

Contact Information for Business Card

LOGO
baseline
Laurent Dufossé
+33(0)6.41.57.09.64
ld@bramleigh-invented.fr
www.bramleigh-invented.fr

Font styles to use
Serif

Colors
cedeed
0255a3
3277b5
85abd2
85cae6
34a7d7
0792cd
cfdeed
1b1b1b

Requirements
Must have
• see description

```html
<!DOCTYPE html>
<html lang="fr">
<head>
<meta charset="utf-8">
<title>BRAMLEIGH – business card</title>
<link rel="stylesheet" href="https://fonts.googleapis.com/css2?family=Questrial&family=Arimo:wght@400&display=swap">
<style>
  :root {
    --page-bg: #e9e7e3;
    --card-bg: #ffffff;
    --card-edge: #dcdcdc;
    --logo-grey: #8c8c8c;
    --brand-blue: #0255a3;
    --baseline-blue: #3277b5;
    --ink: #1b1b1b;
  }
  * { box-sizing: border-box; margin: 0; padding: 0; }
  html, body { width: 1200px; height: 902px; overflow: hidden; }
  body {
    background: var(--page-bg);
    display: flex;
    flex-direction: column;
    align-items: center;
    justify-content: center;
    gap: 40px;
  }
  .card {
    width: 560px;
    height: 340px;
    background: linear-gradient(160deg, #ffffff 0%, #f6f6f6 100%);
    border: 1px solid var(--card-edge);
    box-shadow: 0 6px 18px rgba(0,0,0,0.18);
    position: relative;
  }
  .brand {
    display: flex;
    flex-direction: column;
    align-items: flex-start;
  }
  .brand-name {
    font-family: "Questrial", sans-serif;
    font-weight: 400;
    color: var(--logo-grey);
    letter-spacing: 0.08em;
    line-height: 1;
  }
  .brand-baseline {
    font-family: "Questrial", sans-serif;
    color: var(--baseline-blue);
    letter-spacing: 0.06em;
    margin-top: 4px;
  }
  /* front */
  .card-front .brand {
    position: absolute;
    left: 50%;
    top: 50%;
    transform: translate(-50%, -50%);
  }
  .card-front .brand-name { font-size: 46px; }
  .card-front .brand-baseline { font-size: 16px; align-self: flex-end; }
  /* back */
  .card-back .brand {
    position: absolute;
    left: 40px;
    top: 38px;
  }
  .card-back .brand-name { font-size: 34px; }
  .card-back .brand-baseline { font-size: 13px; align-self: flex-end; }
  .holder-name {
    position: absolute;
    right: 40px;
    top: 120px;
    font-family: "Arimo", sans-serif;
    font-size: 22px;
    color: var(--ink);
  }
  .contact-list {
    position: absolute;
    right: 40px;
    top: 172px;
    list-style: none;
    display: flex;
    flex-direction: column;
    align-items: flex-end;
    gap: 9px;
  }
  .contact-item {
    display: flex;
    align-items: center;
    gap: 10px;
    font-family: "Arimo", sans-serif;
    font-size: 15px;
    color: var(--ink);
  }
  .contact-icon { width: 18px; height: 18px; display: block; }
</style>
</head>
<body>
  <section class="card card-front" aria-label="Card front">
    <div class="brand">
      <span class="brand-name">BRAMLEIGH</span>
      <span class="brand-baseline">real estate family office</span>
    </div>
  </section>

  <section class="card card-back" aria-label="Card back">
    <div class="brand">
      <span class="brand-name">BRAMLEIGH</span>
      <span class="brand-baseline">real estate family office</span>
    </div>
    <p class="holder-name">Laurent Dufossé</p>
    <ul class="contact-list">
      <li class="contact-item">
        <span>+33(0)6.41.57.09.64</span>
        <svg class="contact-icon" viewBox="0 0 18 18" aria-hidden="true">
          <rect width="18" height="18" fill="#0255a3"/>
          <path d="M5 4 L7.5 4 L8.3 6.8 L7 8 Q8.3 10.5 10 11 L11.2 9.7 L14 10.5 L14 13 Q9 13.6 6.5 10.5 Q4.4 8 5 4 Z" fill="#fff"/>
        </svg>
      </li>
      <li class="contact-item">
        <span>www.bramleigh-invented.fr</span>
        <svg class="contact-icon" viewBox="0 0 18 18" aria-hidden="true">
          <rect width="18" height="18" fill="#0255a3"/>
          <circle cx="9" cy="9" r="5" fill="none" stroke="#fff" stroke-width="1.3"/>
          <ellipse cx="9" cy="9" rx="2.2" ry="5" fill="none" stroke="#fff" stroke-width="1"/>
          <line x1="4" y1="9" x2="14" y2="9" stroke="#fff" stroke-width="1"/>
        </svg>
      </li>
      <li class="contact-item">
        <span>ld@bramleigh-invented.fr</span>
        <svg class="contact-icon" viewBox="0 0 18 18" aria-hidden="true">
          <rect width="18" height="18" fill="#0255a3"/>
          <rect x="3.5" y="5" width="11" height="8" fill="none" stroke="#fff" stroke-width="1.2"/>
          <path d="M3.5 5 L9 9.5 L14.5 5" fill="none" stroke="#fff" stroke-width="1.2"/>
        </svg>
      </li>
    </ul>
  </section>
</body>
</html>
```